Meridian Lodging Partners

An Editable Business Card Template For MLP & MLH
Similar or Different Design

418 W. Harlan Brookside Pkwy.
Suite 2270
Irving, TX 75091

```html
<!DOCTYPE html>
<html lang="en">
<head>
<meta charset="utf-8">
<title>Meridian Lodging Partners – Business Card</title>
<link rel="stylesheet" href="https://fonts.googleapis.com/css2?family=Arimo:wght@400;700&family=Cinzel:wght@400;600&display=swap">
<style>
  :root {
    --stage: #121212;
    --card: #2a2a2c;
    --card-edge: #b3141a;
    --brand-red: #c0282b;
    --ink: #f2f2f2;
    --ink-muted: #8a8a8c;
  }
  * { margin: 0; padding: 0; box-sizing: border-box; }
  html, body { width: 1200px; height: 820px; overflow: hidden; }
  body {
    background: var(--stage);
    display: flex; align-items: center; justify-content: center; gap: 40px;
    font-family: "Arimo", Arial, sans-serif;
    color: var(--ink);
  }
  .card {
    position: relative;
    width: 540px; height: 309px;
    background: var(--card);
    border: 3px solid var(--card-edge);
    border-radius: 3px;
    box-shadow: 0 18px 40px rgba(0,0,0,.6);
  }
  /* Front */
  .brand-name {
    position: absolute; top: 62px; left: 250px;
    width: 220px;
    font-family: "Arimo", Arial, sans-serif; font-weight: 700;
    font-size: 22px; line-height: 1.25; color: var(--ink);
  }
  .address {
    position: absolute; right: 36px; top: 160px;
    text-align: right; font-size: 14px; line-height: 1.3; font-style: normal;
  }
  .person { position: absolute; left: 36px; top: 150px; }
  .person-name {
    font-family: "Cinzel", serif; font-weight: 600;
    font-size: 19px; color: var(--brand-red); letter-spacing: .5px;
  }
  .person-role { font-size: 13px; margin-top: 2px; }
  .contact {
    position: absolute; left: 36px; top: 206px;
    list-style: none; font-size: 12.5px; line-height: 1.4;
  }
  .contact li { display: flex; align-items: center; gap: 8px; }
  .contact svg { width: 11px; height: 11px; fill: none; stroke: var(--brand-red); stroke-width: 2; }
  /* Back */
  .card-back .brand-name {
    left: 0; right: 0; width: auto; top: 70px;
    text-align: center; color: var(--ink-muted); font-size: 24px;
  }
  .tagline {
    position: absolute; left: 0; right: 0; top: 170px;
    text-align: center; font-size: 11.5px; line-height: 1.5;
  }
</style>
</head>
<body>
  <section class="card card-front">
    <div class="brand-name">Meridian Lodging Partners</div>
    <address class="address">
      418 W. Harlan Brookside Pkwy.<br>Suite 2270<br>Irving, TX 75091
    </address>
    <div class="person">
      <div class="person-name">Daniel Whitford</div>
      <div class="person-role">Sales Manager</div>
    </div>
    <ul class="contact">
      <li><svg viewBox="0 0 12 12"><path d="M2 1l2.5 0 1 3-1.5 1a6 6 0 0 0 3 3l1-1.5 3 1V10a1 1 0 0 1-1 1A9 9 0 0 1 1 2a1 1 0 0 1 1-1z"/></svg>214-555-0147</li>
      <li><svg viewBox="0 0 12 12"><rect x="3" y="1" width="6" height="10" rx="1"/></svg>480-555-0193</li>
      <li><svg viewBox="0 0 12 12"><rect x="1" y="2.5" width="10" height="7"/><path d="M1 2.5l5 4 5-4"/></svg>dwhitford@meridianlodging.com</li>
      <li><svg viewBox="0 0 12 12"><circle cx="6" cy="6" r="5"/><path d="M1 6h10M6 1c-2.5 3-2.5 7 0 10M6 1c2.5 3 2.5 7 0 10"/></svg>www.MLPOilField.com</li>
    </ul>
  </section>

  <section class="card card-back">
    <div class="brand-name">Meridian Lodging Partners</div>
    <p class="tagline">
      Experienced Provider to Oil, Gas, Energy &amp; Construction Industries<br>
      Consolidated Billing | Full Service Corporate Lodging<br>
      Live Customer Support 24/7/365 | Proven Track Record Of Performance<br>
      Best Negotiated Rates &amp; No Additional Fees
    </p>
  </section>
</body>
</html>
```